MAPLE Quarters One-Page Inserts

We need TWO one-page insert for a transplant display stand (6"x8"). We have a few furnished apartments and we need to inform our guests about the services available:

Insert #1: Delivery and Pickup Services in the neighborhood (Laundry, Groceries, Restaurants).
Insert #1 Text: "Heading: Pick and Delivery Services in your neighborhood:" Text below it: "1) Laundry Pickup - Call: +9714-382-6047. 2) Groceries Delivery - Call: +9714-382-6047, 3) Restaurants Delivery - Call: +9714-382-6047"

Insert #2: We also need another one-page insert to encourage the guests to enjoy the candles and to make the apartment have a homier feeling.
Insert #2 Text: "Heading: Feel at home. Text below it: "Dim the lights, light up a candle, play nice music, have a relaxing stay."

Target Market(s)

Staynook Users. Apartment Guests. Tourist. Age Group 20 to 60 years old.

Industry/Entity Type

Hotel

Requirements
Must have
• - The Company logo of MAPLE Quarters must be displayed on the upper corner. (Logo attached). The logo should be a single color either white or black (Not red and black or red and white)
• For Insert # 1: Laundry, Groceries, and Breakfast Resturaunts images or icons. The images/icons must be unified and look like from the same family of images/icons.
• For Insert # 2: A romantic candle(s) dinner pictures.
Nice to have
• Not too many colors
• Not too busy
• Simple
• Eye Catchy
Should not have
• Lots of colors
• Too many images
• Too Busy

```html
<!DOCTYPE html>
<html lang="en">
<head>
<meta charset="utf-8">
<title>MAPLE Quarters Inserts</title>
<link rel="stylesheet" href="https://fonts.googleapis.com/css2?family=Lato:wght@300;400;700&family=Pinyon+Script&display=swap">
<style>
  :root {
    --page-bg: #dcdcdc;
    --ink-light: #ffffff;
    --ink-soft: #f1f1f1;
    --pill-bg: #ececec;
    --pill-ink: #222222;
    --street-dark: #323236;
    --street-mid: #5d6170;
    --street-glow: #8a8580;
    --candle-top: #4a4641;
    --candle-mid: #5a5650;
    --candle-low: #8f8a80;
  }
  * { box-sizing: border-box; margin: 0; padding: 0; }
  html, body {
    width: 1200px; height: 785px; overflow: hidden;
    background: var(--page-bg);
    font-family: "Lato", sans-serif;
  }
  .insert {
    position: absolute; top: 78px;
    width: 468px; height: 622px;
    overflow: hidden; color: var(--ink-light);
  }
  .insert--services { left: 90px; }
  .insert--home { left: 627px; }
  .insert__photo { position: absolute; inset: 0; }
  .insert--services .insert__photo {
    background:
      radial-gradient(ellipse 60% 40% at 75% 30%, rgba(170,150,120,.55), transparent 70%),
      linear-gradient(100deg, var(--street-dark) 0%, var(--street-dark) 25%, var(--street-mid) 60%, var(--street-glow) 100%);
  }
  .insert--home .insert__photo {
    background:
      radial-gradient(ellipse 70% 35% at 55% 82%, rgba(200,190,170,.55), transparent 75%),
      linear-gradient(180deg, var(--candle-top) 0%, var(--candle-mid) 55%, var(--candle-low) 100%);
  }
  .brand {
    position: absolute; top: 34px; right: 18px;
    font-size: 34px; font-weight: 400; letter-spacing: 1px;
    color: var(--ink-light);
  }
  .services__title {
    position: absolute; top: 136px; left: 0; width: 100%;
    text-align: center; font-size: 29px; font-weight: 400; letter-spacing: .3px;
  }
  .services__subtitle {
    position: absolute; top: 186px; left: 0; width: 100%;
    text-align: center; font-size: 15px; font-weight: 300;
  }
  .service {
    position: absolute; top: 268px; width: 150px; margin-left: -75px;
    text-align: center;
  }
  .service--laundry { left: 82px; }
  .service--groceries { left: 231px; }
  .service--restaurants { left: 387px; }
  .service__icon { display: block; margin: 0 auto; width: 94px; height: 94px; }
  .service__name {
    margin-top: 14px; font-size: 12.5px; font-weight: 700; letter-spacing: .2px;
  }
  .service__phone {
    margin-top: 6px; font-size: 12px; font-weight: 400;
    display: flex; align-items: center; justify-content: center; gap: 3px;
  }
  .service__phone svg { width: 11px; height: 11px; }
  .services__more {
    position: absolute; top: 476px; left: 0; width: 100%;
    text-align: center; font-size: 14.5px; font-weight: 400;
  }
  .site-pill {
    position: absolute; top: 546px; left: 117px;
    width: 235px; height: 26px; border-radius: 8px;
    background: var(--pill-bg); color: var(--pill-ink);
    font-size: 16px; text-align: center; line-height: 26px;
  }
  .home__title {
    position: absolute; top: 128px; left: 0; width: 100%;
    text-align: center; font-family: "Pinyon Script", cursive;
    font-size: 66px; font-weight: 400; color: var(--ink-light);
  }
  .home__text {
    position: absolute; top: 222px; left: 0; width: 100%;
    text-align: center; font-size: 19.5px; font-weight: 300;
    line-height: 29px; color: var(--ink-soft);
  }
</style>
</head>
<body>

<section class="insert insert--services">
  <div class="insert__photo" role="img" aria-label="Photo of a person with an umbrella on a rainy city street with blurred lights"></div>
  <div class="brand">MAPLE</div>
  <h1 class="services__title">PICK AND DELIVERY SERVICES</h1>
  <p class="services__subtitle">IN YOUR NEIGHBORHOOD</p>

  <div class="service service--laundry">
    <svg class="service__icon" viewBox="0 0 94 94" aria-hidden="true">
      <circle cx="47" cy="47" r="44" fill="none" stroke="#fff" stroke-width="4"/>
      <path d="M47 22 a3.5 3.5 0 1 1 3 4 v4" fill="none" stroke="#fff" stroke-width="1.8"/>
      <path d="M47 30 L26 44 H68 Z" fill="none" stroke="#fff" stroke-width="2.5" stroke-linejoin="round"/>
      <rect x="32" y="44" width="30" height="26" fill="#fff"/>
    </svg>
    <div class="service__name">LAUNDRY PICKUP</div>
    <div class="service__phone">
      <svg viewBox="0 0 12 12" aria-hidden="true"><circle cx="6" cy="6" r="5.2" fill="none" stroke="#fff" stroke-width="1"/><path d="M4 3.2 l1 1.6 -.6 .7 a4 4 0 0 0 2.1 2.1 l.7-.6 1.6 1 -.6 1 C6 9 3 6 3.2 4 Z" fill="#fff"/></svg>
      +9714-382-6047
    </div>
  </div>

  <div class="service service--groceries">
    <svg class="service__icon" viewBox="0 0 94 94" aria-hidden="true">
      <circle cx="47" cy="47" r="44" fill="none" stroke="#fff" stroke-width="4"/>
      <rect x="40" y="24" width="6" height="22" fill="#fff"/>
      <rect x="50" y="20" width="7" height="26" rx="3" fill="#fff"/>
      <path d="M33 30 l6 16" stroke="#fff" stroke-width="3"/>
      <path d="M30 44 H64 L61 70 H33 Z" fill="#fff"/>
      <path d="M30 50 c-6 0 -6 12 3 14 M64 50 c6 0 6 12 -3 14" fill="none" stroke="#fff" stroke-width="2.5"/>
    </svg>
    <div class="service__name">GROCERIES DELIVERY</div>
    <div class="service__phone">
      <svg viewBox="0 0 12 12" aria-hidden="true"><circle cx="6" cy="6" r="5.2" fill="none" stroke="#fff" stroke-width="1"/><path d="M4 3.2 l1 1.6 -.6 .7 a4 4 0 0 0 2.1 2.1 l.7-.6 1.6 1 -.6 1 C6 9 3 6 3.2 4 Z" fill="#fff"/></svg>
      +9714-382-6047
    </div>
  </div>

  <div class="service service--restaurants">
    <svg class="service__icon" viewBox="0 0 94 94" aria-hidden="true">
      <circle cx="47" cy="47" r="44" fill="none" stroke="#fff" stroke-width="4"/>
      <circle cx="47" cy="30" r="3" fill="#fff"/>
      <path d="M24 58 a23 23 0 0 1 46 0 Z" fill="#fff"/>
      <rect x="20" y="61" width="54" height="4" fill="#fff"/>
    </svg>
    <div class="service__name">RESTAURANTS DELIVERY</div>
    <div class="service__phone">
      <svg viewBox="0 0 12 12" aria-hidden="true"><circle cx="6" cy="6" r="5.2" fill="none" stroke="#fff" stroke-width="1"/><path d="M4 3.2 l1 1.6 -.6 .7 a4 4 0 0 0 2.1 2.1 l.7-.6 1.6 1 -.6 1 C6 9 3 6 3.2 4 Z" fill="#fff"/></svg>
      +9714-382-6047
    </div>
  </div>

  <p class="services__more">For more info, visit our website or call +9714-382-6040</p>
  <div class="site-pill">www.maplequarters.com</div>
</section>

<section class="insert insert--home">
  <div class="insert__photo" role="img" aria-label="Photo of lit white pillar candles and a smooth stone on a wooden surface"></div>
  <div class="brand">MAPLE</div>
  <h1 class="home__title">Feel At Home</h1>
  <p class="home__text">Dim the lights, light up a candle,<br>play nice music, have a relaxing stay.</p>
  <div class="site-pill">www.maplequarters.com</div>
</section>

</body>
</html>
```